Back Pain

Need a flyer similar to the attached draft. This is to be handed out to prospective patients. Note that Sketch Hive has already designed the logo. If you need a copy please contact me

```html
<!DOCTYPE html>
<html lang="en">
<head>
<meta charset="utf-8">
<title>Back Pain Relief Clinic Flyer</title>
<link href="https://fonts.googleapis.com/css2?family=Raleway:wght@500;600;800&family=Teko:wght@400;500&display=swap" rel="stylesheet">
<style>
  :root {
    --page: #15142f;
    --paper: #b9e1ea;
    --paper-light: #cdebf1;
    --orange: #e9573a;
    --red: #dc3430;
    --deep-red: #c9262a;
    --teal: #2a9db5;
    --teal-dark: #1f8fa9;
    --teal-pill: #5aaec2;
    --pill-text: #eaf6f9;
    --white: #ffffff;
  }
  html, body {
    margin: 0;
    width: 1200px;
    height: 906px;
    overflow: hidden;
    background: var(--page);
  }
  .flyer {
    position: absolute;
    left: 280px;
    top: 26px;
    width: 640px;
    height: 854px;
    background: linear-gradient(160deg, var(--paper-light), var(--paper));
    overflow: hidden;
    font-family: "Raleway", sans-serif;
  }
  .figure-art {
    position: absolute;
    left: 0; top: 120px; width: 300px; height: 390px;
    z-index: 0;
    background: radial-gradient(ellipse at 35% 40%, #2c93ad 0%, #5fb1c6 55%, rgba(185,225,234,0) 80%);
  }
  .banner {
    position: absolute;
    z-index: 2;
    margin: 0;
    color: var(--white);
    font-weight: 800;
    font-size: 34px;
    line-height: 1;
    display: flex;
    align-items: center;
  }
  .banner--top {
    left: 0; top: 9px; width: 432px; height: 44px;
    background: linear-gradient(90deg, var(--orange), #ea5a34);
    border-radius: 0 22px 22px 0;
    justify-content: flex-end;
    padding-right: 18px;
    box-sizing: border-box;
  }
  .banner--sub {
    left: 172px; top: 64px; width: 468px; height: 44px;
    background: var(--red);
    border-radius: 22px 0 0 22px;
    padding-left: 18px;
    box-sizing: border-box;
  }
  .symptom {
    position: absolute;
    z-index: 1;
    height: 43px;
    background: var(--teal-pill);
    color: var(--pill-text);
    font-family: "Teko", sans-serif;
    font-size: 38px;
    line-height: 47px;
    border-radius: 0 22px 22px 0;
    padding: 0 12px;
    box-sizing: border-box;
    text-align: right;
    white-space: nowrap;
  }
  .chart-title {
    position: absolute;
    z-index: 1;
    left: 434px; top: 136px;
    font-family: "Teko", sans-serif;
    color: var(--red);
    font-size: 21px;
    line-height: 24px;
    margin: 0;
    text-transform: uppercase;
  }
  .chart {
    position: absolute;
    z-index: 1;
    left: 0; top: 0;
  }
  .stat {
    position: absolute;
    z-index: 1;
    left: 398px; top: 438px;
    color: var(--teal);
  }
  .stat__lead, .stat__tail {
    font-size: 13px;
    font-weight: 500;
    margin: 0;
    letter-spacing: -0.2px;
  }
  .stat__pill {
    display: inline-block;
    margin: 2px 0 2px -6px;
    background: var(--red);
    color: var(--white);
    font-weight: 800;
    font-size: 19px;
    padding: 2px 12px 2px 6px;
    border-radius: 0 14px 14px 0;
  }
  .care-copy {
    position: absolute;
    left: 31px; top: 554px;
    margin: 0;
    color: var(--teal);
    font-size: 17px;
    line-height: 23px;
    font-weight: 500;
    text-transform: uppercase;
  }
  .doctor {
    position: absolute;
    left: 0; top: 642px; width: 496px; height: 53px;
    background: var(--deep-red);
    border-radius: 0 27px 27px 0;
    color: var(--white);
    font-weight: 800;
    font-size: 34px;
    line-height: 53px;
    padding-left: 31px;
    box-sizing: border-box;
    margin: 0;
  }
  .offer {
    position: absolute;
    left: 0; top: 713px; width: 640px; height: 141px;
    background: linear-gradient(90deg, var(--teal-dark), var(--teal));
    border-radius: 0 48px 0 0;
    color: var(--white);
    padding: 14px 0 0 31px;
    box-sizing: border-box;
    font-size: 29px;
    line-height: 35px;
    font-weight: 500;
    text-transform: uppercase;
    margin: 0;
  }
  .offer strong { font-weight: 800; }
</style>
</head>
<body>
<main class="flyer">
  <div class="figure-art" role="img" aria-label="Illustration of a person's torso silhouette with a highlighted spine and pain markers on the lower back"></div>

  <h1 class="banner banner--top">BACK PAIN</h1>
  <h2 class="banner banner--sub">RELIEF CLINIC</h2>

  <span class="symptom" style="left:112px;top:155px;width:166px;">HEADACHES</span>
  <span class="symptom" style="left:176px;top:211px;width:213px;">SHOULDERPAIN</span>
  <span class="symptom" style="left:231px;top:266px;width:141px;">NECKPAIN</span>
  <span class="symptom" style="left:236px;top:320px;width:145px;">BACKPAIN</span>
  <span class="symptom" style="left:184px;top:375px;width:227px;">ARM&amp;HANDPAIN</span>
  <span class="symptom" style="left:159px;top:427px;width:132px;">SCIATICA</span>

  <p class="chart-title">As the head tilts forward<br>more force is placed<br>on the spine</p>

  <svg class="chart" width="640" height="520" viewBox="0 0 640 520" aria-label="Bar chart of force on the spine by degree of forward head tilt">
    <g fill="#e0433a">
      <path d="M432.5 309 V298 a14.5 14.5 0 0 1 29 0 V309 Z"/>
      <path d="M471.5 309 V255 a14.5 14.5 0 0 1 29 0 V309 Z"/>
      <path d="M511.5 309 V223 a14.5 14.5 0 0 1 29 0 V309 Z"/>
      <path d="M551.5 309 V202 a14.5 14.5 0 0 1 29 0 V309 Z"/>
      <path d="M591.5 309 V172 a14.5 14.5 0 0 1 29 0 V309 Z"/>
    </g>
    <rect x="428" y="307" width="196" height="3" fill="#e0433a"/>
    <g font-family="Teko, sans-serif" font-size="20" fill="#ffffff" text-anchor="middle">
      <text x="447" y="304">12</text>
      <text x="486" y="268">27</text>
      <text x="526" y="236">40</text>
      <text x="566" y="215">49</text>
      <text x="606" y="185">60</text>
    </g>
    <g font-family="Teko, sans-serif" font-size="20" fill="#2a9db5" text-anchor="middle">
      <text x="447" y="332">0</text>
      <text x="486" y="332">15</text>
      <text x="526" y="332">30</text>
      <text x="566" y="332">45</text>
      <text x="606" y="332">60</text>
    </g>
    <text x="434" y="354" font-family="Teko, sans-serif" font-size="19" fill="#dc3430">DEGREES OF FORWARD HEAD TILT</text>
    <circle cx="360" cy="467" r="32" fill="#dc3430"/>
    <path d="M360 441 L348 465 L360 493 A26 26 0 0 1 360 441 Z" fill="#b9e1ea"/>
  </svg>

  <div class="stat">
    <p class="stat__lead">THE AVERAGE PERSON SPENDS</p>
    <span class="stat__pill">8-11 HOURS PER DAY</span>
    <p class="stat__tail">USING ELECTRONIC DEVICES</p>
  </div>

  <p class="care-copy">Chiropractic care can her..<br>correct and prevent these problem by restoring and<br>maintainin proper alignment of the...</p>

  <h3 class="doctor">DR.MARTIN HALE</h3>

  <p class="offer">Now in Bayview at 42 Harbour Rd.<br><strong>50%</strong> off initial consultation if you<br>book <strong>online</strong> at <strong>www.backease.com</strong></p>
</main>
</body>
</html>
```